Create Banner Ads for Steeple Trade Register

The orginal web page design project was cancelled and we are looking to use our remaining allocated funds for Banner Ad designs.

We need the designer to create 300x250 and matching 300x125 Banner Ads promoting PewMarket.com. Please look at website home page with priest (will provide photo). The banner ads will be used on other religious websites to get visitors to click and visit http://PewMarket.com and find businesses who support Catholic churches.

"Find a Business Supporting Your Church"

Can use other images than those provided. For example religious background or image of church, etc.

Would also like to see a new simple logo graphic for "Steeple Trade Locator" included on this project.

Thanks. -ray
Updates

Project Deadline Extended Reason: The original web page design project was cancelled and we are wanting to use our remaining funds for nice Banner Ad designs promoting our website http://pewmarket.com Added Sunday, January 3, 2016

Target Market(s)

Catholics looking for businesses who support the church.

Industry/Entity Type

Religious

Coding

Coded - Design and coding required

Number of Pages Required

1 page

Font styles to use
Serif

Requirements
Must have
• Attractive Clean Appearance.

```html
<!DOCTYPE html>
<html lang="en">
<head>
<meta charset="utf-8">
<title>Steeple Trade Locator – Logo and Banner Ads</title>
<link rel="stylesheet" href="https://fonts.googleapis.com/css2?family=Crimson+Text:wght@400;600&family=Noto+Serif:wght@700&family=Tinos:wght@400;700&family=Open+Sans:wght@400&display=swap">
<style>
  :root {
    --navy: #26497a;
    --navy-deep: #1f3d66;
    --teal: #3a7d99;
    --grey-text: #9a9a9a;
    --grey-label: #a5a5a5;
    --curve-line: #9b9b9b;
    --white: #ffffff;
    --frame: #2f5a8c;
    --wood-dark: #3a1f10;
    --wood-mid: #6b3f22;
    --wood-light: #8a5832;
  }
  * { box-sizing: border-box; margin: 0; padding: 0; }
  html, body { width: 1000px; height: 1200px; overflow: hidden; background: var(--white); }
  .sheet {
    position: relative; width: 1000px; height: 1200px;
    border: 1px solid var(--frame); background: var(--white);
  }
  .brand { position: absolute; display: flex; align-items: center; }
  .brand-dot { border-radius: 50%; background: var(--navy); flex: none; }
  .brand-name {
    font-family: "Crimson Text", serif; font-weight: 400; color: var(--teal);
    line-height: 1;
  }
  .brand--main { left: 48px; top: 128px; gap: 24px; }
  .brand--main .brand-dot { width: 92px; height: 92px; }
  .brand--main .brand-name { font-size: 46px; }
  .brand--main .brand-name span { display: block; }
  .brand--main .brand-name span + span { padding-left: 100px; margin-top: 2px; }

  .favicon-label {
    position: absolute; left: 637px; top: 162px;
    font-family: "Open Sans", sans-serif; font-size: 38px; color: var(--grey-label);
  }
  .favicon-tile {
    position: absolute; left: 848px; top: 147px; width: 71px; height: 72px;
    border-radius: 7px; background: linear-gradient(#2f5a8f, var(--navy-deep));
    box-shadow: 0 3px 2px rgba(0,0,0,.25);
  }

  .showcase {
    position: absolute; left: 18px; top: 321px; width: 960px; height: 673px;
    background: linear-gradient(100deg, var(--wood-dark) 0%, var(--wood-mid) 35%, var(--wood-light) 55%, var(--wood-mid) 75%, var(--wood-dark) 100%);
  }

  .banner { position: absolute; background: var(--white); overflow: hidden; }
  .banner svg.sweep { position: absolute; inset: 0; }
  .banner .brand-name { color: var(--teal); }
  .headline {
    position: absolute; font-family: "Noto Serif", serif; font-weight: 700;
    color: var(--grey-text); line-height: 1.3;
  }
  .cta {
    position: absolute; display: flex; align-items: center; justify-content: center;
    background: linear-gradient(#2e578b, var(--navy-deep)); color: var(--white);
    font-family: "Tinos", serif; font-weight: 700; border-radius: 4px;
    box-shadow: 0 2px 2px rgba(0,0,0,.35);
  }
  .phone {
    position: absolute; font-family: "Tinos", serif; color: var(--white);
  }

  .banner--square { left: 274px; top: 369px; width: 424px; height: 353px; }
  .banner--square .brand { left: 8px; top: 6px; gap: 14px; }
  .banner--square .brand-dot { width: 72px; height: 72px; }
  .banner--square .brand-name { font-size: 30px; }
  .banner--square .brand-name span { display: block; }
  .banner--square .brand-name span + span { padding-left: 76px; margin-top: 2px; }
  .banner--square .headline { left: 6px; top: 116px; font-size: 24px; }
  .banner--square .cta { left: 31px; top: 232px; width: 130px; height: 41px; font-size: 20px; }
  .banner--square .phone { left: 200px; top: 319px; font-size: 20px; }

  .banner--wide { left: 274px; top: 768px; width: 424px; height: 176px; }
  .banner--wide .brand { left: 13px; top: 6px; gap: 10px; }
  .banner--wide .brand-dot { width: 46px; height: 46px; }
  .banner--wide .brand-name { font-size: 21px; }
  .banner--wide .brand-name span { display: block; }
  .banner--wide .brand-name span + span { padding-left: 52px; margin-top: 1px; }
  .banner--wide .headline { left: 6px; top: 78px; font-size: 22px; line-height: 1.28; }
  .banner--wide .cta { left: 256px; top: 17px; width: 130px; height: 41px; font-size: 20px; }
  .banner--wide .phone { left: 224px; top: 155px; font-size: 17px; }
</style>
</head>
<body>
<main class="sheet">
  <div class="brand brand--main">
    <div class="brand-dot"></div>
    <div class="brand-name"><span>Steeple Trade</span><span>Locator</span></div>
  </div>

  <div class="favicon-label">Favicon:</div>
  <div class="favicon-tile"></div>

  <div class="showcase" role="img" aria-label="Dark weathered wooden plank backdrop"></div>

  <section class="banner banner--square" aria-label="300 by 250 banner ad">
    <svg class="sweep" viewBox="0 0 424 353" width="424" height="353" aria-hidden="true">
      <path d="M424 4 C 405 200, 250 320, 0 353 L424 353 Z" fill="var(--navy)"/>
      <path d="M424 4 C 405 200, 250 320, 0 353" fill="none" stroke="var(--curve-line)" stroke-width="4"/>
    </svg>
    <div class="brand">
      <div class="brand-dot"></div>
      <div class="brand-name"><span>Steeple Trade</span><span>Locator</span></div>
    </div>
    <h2 class="headline">Find a Business Supporting<br>&nbsp;Your Church</h2>
    <a class="cta">contact us</a>
    <p class="phone">Call us:1-800-555-0142</p>
  </section>

  <section class="banner banner--wide" aria-label="300 by 125 banner ad">
    <svg class="sweep" viewBox="0 0 424 176" width="424" height="176" aria-hidden="true">
      <path d="M424 6 C 400 110, 260 165, 0 176 L424 176 Z" fill="var(--navy)"/>
      <path d="M424 6 C 400 110, 260 165, 0 176" fill="none" stroke="var(--curve-line)" stroke-width="4"/>
    </svg>
    <div class="brand">
      <div class="brand-dot"></div>
      <div class="brand-name"><span>Steeple Trade</span><span>Locator</span></div>
    </div>
    <a class="cta">contact us</a>
    <h2 class="headline">Find a Business Supporting<br>&nbsp;Your Church</h2>
    <p class="phone">Call us:1-800-555-0142</p>
  </section>
</main>
</body>
</html>
```